BRINDLEWAVE is a New Zealand based aerial imaging company performing mapping, surveying and videography

I would like a business card that is contemporary and clean. The font for the business name is called Gtec Technology and I would like to have the text "AERIAL IMAGING" under the "BRINDLEWAVE" name in a font similar to URW Gothic or another light modern font. Brindlewave performs aerial imaging projects using a hexacopter UAV. Surveying and mapping with 3D Digital Elevation Models are a focus, I also produce aerial photographs and video's including post editing.
Updates

Target Market(s)

Industrial plant managers, Property owners, Event organisers.

Industry/Entity Type

Videography

Contact Information for Business Card

BRINDLEWAVE AERIAL IMAGING. Owner Ross Pellow. Cell: 027 4913068. P.O. Box 8321 Dunedin, New Zealand.

Font styles to use
Other font styles liked:
• Gtec Technology

Colors
9bcb3b
33a6d7
ec1f27

Requirements
Must have
• Modern professional look.
Nice to have
• Perhaps an aerial image of a landscape who's location is not identifiable. Maybe use included image of my hexacopter on the back of the card? Not compulsory though.
Should not have
• Clip Art style images.

```html
<!DOCTYPE html>
<html lang="en">
<head>
<meta charset="UTF-8">
<title>Brindlewave Aerial Imaging – Business Card</title>
<link rel="stylesheet" href="https://fonts.googleapis.com/css2?family=Didact+Gothic&display=swap">
<style>
  :root {
    --page-bg: #ffffff;
    --sky-light: #cfd4ea;
    --sky-mid: #a9acd8;
    --hill-purple: #4b3f9a;
    --hill-green: #3f8f8a;
    --brand-blue: #33a6d7;
    --ring-pale: #d4d6ec;
    --text-white: #ffffff;
  }
  * { margin: 0; padding: 0; box-sizing: border-box; }
  html, body {
    width: 1200px;
    height: 1000px;
    overflow: hidden;
    background: var(--page-bg);
  }
  .business-card {
    position: absolute;
    left: 181px;
    top: 203px;
    width: 840px;
    height: 466px;
    overflow: hidden;
  }
  .landscape-photo {
    position: absolute;
    inset: 0;
    background:
      linear-gradient(180deg,
        var(--sky-light) 0%,
        var(--sky-mid) 30%,
        #8f8cc9 40%,
        var(--hill-purple) 50%,
        #4a47a6 68%,
        var(--hill-green) 88%,
        #5f8a5a 100%);
  }
  .card-graphics {
    position: absolute;
    inset: 0;
  }
  .brand-block {
    position: absolute;
    left: 0;
    width: 840px;
    top: 198px;
    text-align: center;
    font-family: "Didact Gothic", sans-serif;
    color: var(--text-white);
  }
  .brand-name {
    font-size: 44px;
    line-height: 48px;
    letter-spacing: 1px;
  }
  .brand-tagline {
    margin-top: 10px;
    font-size: 31px;
    line-height: 34px;
    letter-spacing: 0.5px;
  }
</style>
</head>
<body>
  <div class="business-card">
    <div class="landscape-photo" role="img" aria-label="Aerial landscape photograph of misty mountains and green valleys under a cloudy sky"></div>
    <svg class="card-graphics" width="840" height="466" viewBox="0 0 840 466" aria-hidden="true">
      <polygon class="accent-band" points="224,0 779,0 619,466 62,466" fill="var(--brand-blue)" fill-opacity="0.88"/>
      <circle class="emblem-ring" cx="422" cy="234" r="203" fill="none" stroke="var(--ring-pale)" stroke-opacity="0.85" stroke-width="28"/>
    </svg>
    <div class="brand-block">
      <div class="brand-name">BRINDLEWAVE</div>
      <div class="brand-tagline">AERIAL IMAGING</div>
    </div>
  </div>
</body>
</html>
```